Sumvera financial services stationery design

We need business stationery designed with letterheads, business cards, with compliments and envelope for a business that offers tax and accounting services
Updates

Designs look the same

Target Market(s)

Small to medium businesses, individuals, Self managed superfunds

Industry/Entity Type

Business

Font styles to use
Serif
Other font styles liked:
• Atlanta

Colors
32a6d6
3277b5

Requirements
Must have
• Logo incorporated with all my stationery
• professional
Should not have
• Lots of colours
• Busy

```html
<!DOCTYPE html>
<html lang="en">
<head>
<meta charset="utf-8">
<title>Sumvera Financial Services – Stationery</title>
<link href="https://fonts.googleapis.com/css2?family=Cinzel:wght@500;600&family=Roboto:wght@400&display=swap" rel="stylesheet">
<style>
:root{
  --stage:#c2c2c2;
  --paper:#f7f7f5;
  --brand:#005ca6;
  --brand-light:#32a6d6;
  --ink:#3a3d40;
  --rule:#3f4245;
}
*{margin:0;padding:0;box-sizing:border-box}
html,body{width:1200px;height:1002px;overflow:hidden}
body{background:var(--stage);position:relative;font-family:"Roboto",sans-serif;color:var(--ink)}
.sheet{position:absolute;background:var(--paper);box-shadow:0 1px 3px rgba(0,0,0,.18);overflow:hidden}
.brand{position:absolute;display:flex;align-items:center;gap:10px}
.brand-mark{background:var(--brand);border-radius:3px;flex:none}
.brand-name{font-family:"Cinzel",serif;font-weight:500;color:var(--ink);letter-spacing:.5px;line-height:1}
.contact{position:absolute;font-size:8px;line-height:11px;color:var(--ink)}
.contact-line{display:flex;align-items:center;gap:6px}
.contact-line svg{width:8px;height:7px;fill:var(--brand-light)}
.footer-band{position:absolute;left:0;bottom:0;width:100%}
.footer-band svg{display:block;width:100%;height:100%}
.footer-url{position:absolute;right:18px;bottom:5px;color:#fff;font-size:8px}

.letterhead{left:118px;top:108px;width:445px;height:630px}
.envelope-front{left:597px;top:139px;width:485px;height:215px}
.envelope-back{left:597px;top:374px;width:485px;height:216px}
.comp-slip{left:617px;top:652px;width:445px;height:210px}
.card-front{left:138px;top:776px;width:192px;height:116px;background:var(--brand)}
.card-back{left:349px;top:776px;width:193px;height:116px}

.flap{position:absolute;left:0;top:0;width:100%;height:80px}
.flap-url{position:absolute;left:0;right:0;top:33px;text-align:center;color:#fff;font-size:9px;letter-spacing:1px}
.compliments{position:absolute;right:19px;top:37px;font-family:"Cinzel",serif;font-weight:600;font-size:11px;color:var(--brand);letter-spacing:.5px}
.holder-name{position:absolute;left:11px;top:55px;font-family:"Cinzel",serif;font-weight:600;font-size:7.5px;color:var(--brand);letter-spacing:.4px}
.holder-role{position:absolute;left:11px;top:65px;font-size:3.5px;color:var(--ink)}
</style>
</head>
<body>

<svg width="0" height="0" style="position:absolute">
  <defs>
    <symbol id="icon-phone" viewBox="0 0 10 8"><path d="M1 3C1 1 3 0 5 0s4 1 4 3H7V2H3v1zM2 4h6l1 4H1z"/></symbol>
    <symbol id="icon-mail" viewBox="0 0 10 8"><path d="M0 0h10v8H0zM1 1v1l4 3 4-3V1L5 4z"/></symbol>
    <symbol id="band" viewBox="0 0 100 20" preserveAspectRatio="none">
      <rect x="0" y="15" width="100" height="5" fill="#3f4245"/>
      <path d="M55 20C62 9 70 4 76 2H100V20Z" fill="#005ca6"/>
      <path d="M58 20C65 12 72 7 78 5" fill="none" stroke="#f7f7f5" stroke-width="1"/>
      <path d="M60 20C67 13 73 9 79 7" fill="none" stroke="#32a6d6" stroke-width=".6"/>
    </symbol>
  </defs>
</svg>

<!-- Letterhead -->
<section class="sheet letterhead">
  <div class="brand" style="left:35px;top:37px">
    <span class="brand-mark" style="width:40px;height:40px"></span>
    <span class="brand-name" style="font-size:27px">Sumvera</span>
  </div>
  <div class="contact" style="left:29px;top:565px">
    <p>123, Street Number, Your City,</p>
    <p>Your Town, Country 123456</p>
    <p class="contact-line" style="margin-top:3px"><svg><use href="#icon-phone"/></svg>(012) 345 6789</p>
    <p class="contact-line"><svg><use href="#icon-mail"/></svg>alex@sumverafinancial.com</p>
  </div>
  <div class="footer-band" style="height:26px"><svg><use href="#band"/></svg></div>
  <span class="footer-url">www.sumverafinancial.com</span>
</section>

<!-- Envelope front -->
<section class="sheet envelope-front">
  <div class="brand" style="left:23px;top:22px">
    <span class="brand-mark" style="width:37px;height:37px"></span>
    <span class="brand-name" style="font-size:24px">Sumvera</span>
  </div>
  <div class="contact" style="left:22px;top:177px">
    <p>123, Street Number, Your City</p>
    <p>Your Town, Country 123456</p>
  </div>
  <div class="footer-band" style="height:26px"><svg><use href="#band"/></svg></div>
  <span class="footer-url">www.sumverafinancial.com</span>
</section>

<!-- Envelope back -->
<section class="sheet envelope-back">
  <svg class="flap" viewBox="0 0 485 80" preserveAspectRatio="none">
    <path d="M0 0H485L440 69Q432 79 416 79H69Q53 79 45 69Z" fill="var(--brand)"/>
  </svg>
  <span class="flap-url">www.sumverafinancial.com</span>
</section>

<!-- With compliments slip -->
<section class="sheet comp-slip">
  <div class="brand" style="left:19px;top:24px">
    <span class="brand-mark" style="width:38px;height:38px"></span>
    <span class="brand-name" style="font-size:25px">Sumvera</span>
  </div>
  <p class="compliments">With Compliments</p>
  <div class="contact" style="left:19px;top:162px">
    <p class="contact-line"><svg><use href="#icon-phone"/></svg>(012) 345 6789</p>
    <p class="contact-line"><svg><use href="#icon-mail"/></svg>alex@sumverafinancial.com</p>
    <p style="margin-top:2px">123, Street Number, Your City Your Town, Country 123456</p>
  </div>
  <div class="footer-band" style="height:26px"><svg><use href="#band"/></svg></div>
  <span class="footer-url">www.sumverafinancial.com</span>
</section>

<!-- Business card front -->
<section class="sheet card-front">
  <div class="brand" style="left:36px;top:42px">
    <span class="brand-mark" style="width:32px;height:32px;background:#fff"></span>
    <span class="brand-name" style="font-size:20px;color:#fff">Sumvera</span>
  </div>
</section>

<!-- Business card back -->
<section class="sheet card-back">
  <div class="brand" style="right:10px;top:15px;gap:6px">
    <span class="brand-mark" style="width:22px;height:22px"></span>
    <span class="brand-name" style="font-size:14px">Sumvera</span>
  </div>
  <p class="holder-name">Alex Carter</p>
  <p class="holder-role">Managing Partner</p>
  <div class="contact" style="left:11px;top:76px;font-size:4px;line-height:6px">
    <p class="contact-line" style="gap:3px"><svg style="width:4px;height:4px"><use href="#icon-phone"/></svg>(012) 345 6789</p>
    <p class="contact-line" style="gap:3px"><svg style="width:4px;height:4px"><use href="#icon-mail"/></svg>alex@sumverafinancial.com</p>
    <p style="margin-top:3px;line-height:4.5px">123, Street Number, Your City<br>Your Town, Country 123456</p>
  </div>
  <div class="footer-band" style="height:9px"><svg><use href="#band"/></svg></div>
  <span class="footer-url" style="font-size:4px;right:10px;bottom:2px">www.sumverafinancial.com</span>
</section>

</body>
</html>
```